Truck wrap Design For KR CLEANERS

Create unique and eye catching design with provide logo and information.
Also Add Cartoon or silhouette of a men with vacuum or steam cleaner.
Please Use attached template.
It must include logo that is attached. and information below:
--347-555-0142
--www.kettleridgesteamcln.com
--kettleridgec@veltrano.net
-- WQPTA MASKS TEXTILE CLEANER

Services:

Carpet, upholstery, Air duct, Dryer vent, Hard surface cleaning,

Residential/Commercial Services.

Target Market(s)

everyone

Colors

Designer to choose colors to be used in the design.

Requirements
Must have
• All the information that is provide in descricption
Should not have
• silly background.

```html
<!DOCTYPE html>
<html lang="en">
<head>
<meta charset="utf-8">
<title>KR Cleaners Truck Wrap Side Panel</title>
<link href="https://fonts.googleapis.com/css2?family=Roboto+Slab:wght@800&family=Saira+Condensed:wght@800&family=Ubuntu:wght@500&display=swap" rel="stylesheet">
<style>
  :root {
    --teal: #0aa19c;
    --green: #10a650;
    --green-deep: #0c9a45;
    --purple: #5b3fa0;
    --pink: #ea1f7a;
    --coral: #f0405a;
    --white: #ffffff;
    --page: #ffffff;
  }
  * { margin: 0; padding: 0; box-sizing: border-box; }
  html, body { width: 1200px; height: 1200px; overflow: hidden; background: var(--page); }
  .wrap-panel {
    position: absolute; left: 0; top: 223px; width: 1200px; height: 753px;
    overflow: hidden;
    background: linear-gradient(135deg, var(--teal) 0%, var(--green) 55%, var(--green-deep) 100%);
  }
  .halftone-area {
    position: absolute; left: -40px; top: -60px; width: 560px; height: 420px;
    background: radial-gradient(ellipse at 40% 30%, rgba(79,195,242,0.75) 0%, rgba(79,195,242,0.35) 40%, rgba(79,195,242,0) 70%);
  }
  .halftone-area.lower {
    left: 820px; top: 430px; width: 420px; height: 340px;
    background: radial-gradient(ellipse at 50% 60%, rgba(120,220,80,0.55) 0%, rgba(120,220,80,0) 70%);
  }
  .shapes { position: absolute; inset: 0; }
  .phone-ribbon {
    position: absolute; left: 120px; top: 90px;
    font-family: "Saira Condensed", sans-serif; font-weight: 800;
    font-size: 64px; letter-spacing: 2px; color: var(--white);
    transform: rotate(-10deg); transform-origin: left top;
    white-space: nowrap;
  }
  .service-box {
    position: absolute; left: 57px; top: 293px; width: 490px; height: 269px;
    border-radius: 6px;
    background: linear-gradient(135deg, var(--pink) 0%, var(--coral) 100%);
    padding: 30px 0 0 30px;
    z-index: 2;
  }
  .service-title {
    font-family: "Roboto Slab", serif; font-weight: 800;
    font-size: 52px; line-height: 78px; color: var(--white); letter-spacing: 0.5px;
    white-space: nowrap;
  }
  .contact {
    position: absolute; left: 61px; top: 630px;
    font-family: "Ubuntu", sans-serif; font-weight: 500;
    font-size: 31px; line-height: 43px; color: var(--white); letter-spacing: 0.5px;
    white-space: nowrap;
  }
  .brand-badge {
    position: absolute; left: 887px; top: 37px; width: 242px; height: 242px;
    border-radius: 50%; background: var(--white);
    display: flex; align-items: center; justify-content: center; text-align: center;
    z-index: 2;
  }
  .brand-name {
    font-family: "Roboto Slab", serif; font-weight: 800;
    font-size: 30px; line-height: 36px; color: var(--purple);
  }
  .cleaner-illustration {
    position: absolute; left: 575px; top: 300px; width: 555px; height: 450px;
    border-radius: 10px;
    background: linear-gradient(160deg, rgba(91,63,160,0.55) 0%, rgba(30,30,30,0.35) 60%, rgba(255,255,255,0.35) 100%);
  }
</style>
</head>
<body>
  <main class="wrap-panel">
    <div class="halftone-area" role="img" aria-label="Blue halftone dot pattern"></div>
    <div class="halftone-area lower" role="img" aria-label="Light green halftone dot pattern"></div>

    <svg class="shapes" width="1200" height="753" viewBox="0 0 1200 753">
      <line class="accent-stripe" x1="1150" y1="30" x2="760" y2="390" stroke="#5b3fa0" stroke-width="16" stroke-linecap="round"/>
      <line class="accent-stripe" x1="1150" y1="95" x2="880" y2="340" stroke="#5b3fa0" stroke-width="12" stroke-linecap="round"/>
      <polygon class="ribbon" points="90,118 612,35 603,158 85,253" fill="#5b3fa0"/>
      <g fill="#ffffff">
        <polygon points="83,140 89,155 105,155 92,165 97,180 83,171 69,180 74,165 61,155 77,155"/>
        <polygon points="593,120 599,135 615,135 602,145 607,160 593,151 579,160 584,145 571,135 587,135"/>
        <polygon points="48,280 56,299 77,299 60,311 67,331 48,319 29,331 36,311 19,299 40,299"/>
      </g>
    </svg>

    <div class="phone-ribbon">347-555-0142</div>

    <div class="cleaner-illustration" role="img" aria-label="Cartoon of a man in a purple shirt cleaning carpet with a canister vacuum"></div>

    <div class="service-box">
      <p class="service-title">WQPTA MASKS<br>TEXTILE<br>CLEANER</p>
      <svg class="box-stars" width="100" height="50" viewBox="0 0 100 50" style="position:absolute;left:380px;top:236px">
        <g fill="#5b3fa0">
          <polygon points="10,14 15,27 29,27 18,35 22,48 10,40 -2,48 2,35 -9,27 5,27"/>
          <polygon points="56,4 62,20 79,20 65,30 70,46 56,36 42,46 47,30 33,20 50,20"/>
        </g>
      </svg>
    </div>

    <div class="contact">
      <p>www.kettleridgesteamcln.com</p>
      <p>kettleridgec@veltrano.net</p>
    </div>

    <div class="brand-badge">
      <span class="brand-name">KR<br>CLEANERS</span>
    </div>
  </main>
</body>
</html>
```